KB Rubbish Removal Business Card

Hey,
I need a double sided business card designed for a rubbish removal business based in Australia. Logo is already chosen, similar colours preferred for both sides of the business card.

Details to include:

Front:

KB Rubbish Removal
Darren Holloway
Managing Director
Mobile: 0471 902 146
Email: darren@kbrubbishremoval.com.au
Website: kbrubbishremoval.com.au

Rear:

How did we do?
kbrubbishremoval.com.au/review

```html
<!DOCTYPE html>
<html lang="en">
<head>
<meta charset="utf-8">
<title>KB Rubbish Removal – Business Card</title>
<link href="https://fonts.googleapis.com/css2?family=Titillium+Web:wght@700&family=Questrial&display=swap" rel="stylesheet">
<style>
  :root {
    --backdrop: #262626;
    --paper: #ffffff;
    --green-deep: #167533;
    --green-mid: #1f8f41;
    --green-light: #2aa84a;
    --accent-text: #8dc63f;
    --ink: #3a3a3a;
    --ink-soft: #555555;
    --white: #ffffff;
  }
  * { margin: 0; padding: 0; box-sizing: border-box; }
  html, body {
    width: 1200px; height: 900px; overflow: hidden;
    background: var(--backdrop);
  }
  .canvas { position: relative; width: 1200px; height: 900px; }
  .card {
    position: absolute; top: 308px;
    width: 473px; height: 285px;
    background: var(--paper);
    overflow: hidden;
    box-shadow: 0 6px 18px rgba(0,0,0,.55);
  }
  .card--front { left: 97px; }
  .card--back { left: 630px; }
  .card__art { position: absolute; inset: 0; width: 100%; height: 100%; }

  .brand {
    position: absolute; left: 8px; width: 150px; top: 172px;
    display: flex; align-items: center; justify-content: center; gap: 5px;
    font-family: "Questrial", sans-serif; font-weight: 400;
    font-size: 11px; color: var(--ink);
    white-space: nowrap;
  }
  .brand__dot {
    width: 8px; height: 8px; border-radius: 50%; background: var(--green-mid);
    flex: none;
  }

  .person { position: absolute; left: 227px; top: 74px; }
  .person__name {
    font-family: "Titillium Web", sans-serif; font-weight: 700;
    font-size: 24px; line-height: 1; color: var(--accent-text);
    text-transform: uppercase; letter-spacing: -0.3px;
  }
  .person__title {
    margin-top: 3px;
    font-family: "Questrial", sans-serif; font-size: 12.5px;
    color: var(--white); text-transform: uppercase;
  }

  .contacts {
    position: absolute; left: 227px; top: 134px;
    list-style: none;
    font-family: "Questrial", sans-serif; font-size: 13.5px; color: var(--white);
  }
  .contacts__item {
    display: flex; align-items: center; gap: 4px;
    height: 16px; margin-bottom: 13.5px; white-space: nowrap;
  }
  .contacts__icon { width: 16px; height: 16px; flex: none; }

  .review {
    position: absolute; left: 0; width: 278px; top: 125px;
    text-align: center;
  }
  .review__heading {
    font-family: "Titillium Web", sans-serif; font-weight: 700;
    font-size: 22px; line-height: 1; color: var(--accent-text);
    text-transform: uppercase;
  }
  .review__link {
    margin-top: 3px;
    font-family: "Questrial", sans-serif; font-size: 11.5px; color: var(--ink-soft);
  }
</style>
</head>
<body>
<main class="canvas">

  <section class="card card--front" aria-label="Business card front">
    <svg class="card__art" viewBox="0 0 872 526" preserveAspectRatio="none" role="img" aria-label="Green wave artwork panel">
      <defs>
        <linearGradient id="front-panel" x1="0" y1="0" x2="1" y2="1">
          <stop offset="0" stop-color="#2aa84a"/>
          <stop offset="0.4" stop-color="#167533"/>
          <stop offset="1" stop-color="#229944"/>
        </linearGradient>
      </defs>
      <path d="M404,0 Q223,263 404,526 L872,526 L872,0 Z" fill="url(#front-panel)"/>
    </svg>

    <div class="brand"><span class="brand__dot"></span>KB Rubbish Removal</div>

    <div class="person">
      <h1 class="person__name">Darren Holloway</h1>
      <p class="person__title">Managing Director</p>
    </div>

    <ul class="contacts">
      <li class="contacts__item">
        <svg class="contacts__icon" viewBox="0 0 16 16" aria-hidden="true"><circle cx="8" cy="8" r="8" fill="#8dc63f"/><path d="M5 4.2l1.6-.4 1 2.2-1 .8a6 6 0 0 0 2.6 2.6l.8-1 2.2 1-.4 1.6c-3.6.2-7-3.2-6.8-6.8z" fill="#1a7f3a"/></svg>
        0471 902 146
      </li>
      <li class="contacts__item">
        <svg class="contacts__icon" viewBox="0 0 16 16" aria-hidden="true"><circle cx="8" cy="8" r="8" fill="#8dc63f"/><rect x="4" y="5" width="8" height="6" fill="none" stroke="#1a7f3a" stroke-width="1.1"/><path d="M4 5l4 3.3L12 5" fill="none" stroke="#1a7f3a" stroke-width="1"/></svg>
        darren@kbrubbishremoval.com.au
      </li>
      <li class="contacts__item">
        <svg class="contacts__icon" viewBox="0 0 16 16" aria-hidden="true"><circle cx="8" cy="8" r="8" fill="#8dc63f"/><g fill="none" stroke="#1a7f3a" stroke-width="0.9"><circle cx="8" cy="8" r="4.6"/><ellipse cx="8" cy="8" rx="2" ry="4.6"/><path d="M3.4 8h9.2"/></g></svg>
        kbrubbishremoval.com.au
      </li>
    </ul>
  </section>

  <section class="card card--back" aria-label="Business card back">
    <svg class="card__art" viewBox="0 0 872 526" preserveAspectRatio="none" role="img" aria-label="Green wave artwork panel">
      <defs>
        <linearGradient id="back-panel" x1="0" y1="0" x2="1" y2="1">
          <stop offset="0" stop-color="#2aa84a"/>
          <stop offset="0.5" stop-color="#1a8a3c"/>
          <stop offset="1" stop-color="#229944"/>
        </linearGradient>
      </defs>
      <path d="M444,0 Q620,263 444,526 L872,526 L872,0 Z" fill="url(#back-panel)"/>
    </svg>

    <div class="review">
      <h2 class="review__heading">How did we do?</h2>
      <p class="review__link">kbrubbishremoval.com.au/review</p>
    </div>
  </section>

</main>
</body>
</html>
```